Option Sheet

We need a one page option sheet with a left to right reading of the five options. It should be a one sheet, multiple colors and definitive separations between options This is used in a sales consultation. Backround or colors not in option need to have the follow RGB value (5 red, 20 green, 63 blue)

We added a smaller text file, please change that point

Target Market(s)

Divorce

Industry/Entity Type

Legal

Requirements
Must have
• 1) All five options left to right
• 2)language included in sheet

```html
<!DOCTYPE html>
<html lang="en">
<head>
<meta charset="utf-8">
<title>Five Options Divorce</title>
<link rel="stylesheet" href="https://fonts.googleapis.com/css2?family=Barlow:wght@700&family=Arimo:wght@400;700&display=swap">
<style>
  :root {
    --navy: #05143F;
    --odd-tab: #02427A;
    --odd-band: #276B9E;
    --odd-body: #5F8BAF;
    --even-tab: #275F8F;
    --even-band: #437499;
    --even-body: #83A8C2;
    --ink: #FFFFFF;
  }
  * { margin: 0; padding: 0; box-sizing: border-box; }
  html, body { width: 927px; height: 1200px; overflow: hidden; background: var(--navy); }
  .sheet { width: 927px; height: 1200px; font-family: "Arimo", Arial, sans-serif; color: var(--ink); background: var(--navy); }
  .sheet-header { height: 41px; }
  .sheet-title { font-family: "Barlow", sans-serif; font-weight: 700; font-size: 23px; line-height: 43px; padding-left: 37px; letter-spacing: 0.2px; }
  .options { display: flex; gap: 3px; height: 1159px; }
  .option { flex: 1 1 0; display: flex; flex-direction: column; min-width: 0; }
  .option-tab { position: relative; height: 35px; }
  .option-tab svg { position: absolute; left: 0; top: 0; }
  .option-number { position: absolute; left: 12px; top: 0; font-family: "Barlow", sans-serif; font-weight: 700; font-size: 17.5px; line-height: 36px; }
  .option-name { display: flex; align-items: center; height: 52px; padding: 0 12px; font-family: "Barlow", sans-serif; font-weight: 700; font-size: 17.5px; line-height: 21px; }
  .option-body { flex: 1; padding: 10px 10px 0 12px; }
  .odd .option-tab, .odd .option-name { background: var(--odd-band); }
  .odd .option-body { background: var(--odd-body); }
  .even .option-tab, .even .option-name { background: var(--even-band); }
  .even .option-body { background: var(--even-body); }
  .odd .tab { fill: var(--odd-tab); }
  .even .tab { fill: var(--even-tab); }
  .list-heading { font-weight: 700; font-size: 15px; line-height: 20px; }
  .points { list-style: none; margin-bottom: 8px; }
  .points li { position: relative; padding-left: 14px; font-size: 15.5px; line-height: 20.4px; }
  .points li::before { content: ""; position: absolute; left: 2px; top: 9px; width: 4px; height: 4px; border-radius: 50%; background: var(--ink); }
</style>
</head>
<body>
<div class="sheet">
  <header class="sheet-header"><h1 class="sheet-title">Five Options Divorce</h1></header>

  <main class="options">
    <section class="option odd">
      <div class="option-tab">
        <svg width="183" height="35" aria-hidden="true"><polygon class="tab" points="0,0 120,0 130,17.5 120,35 0,35"/></svg>
        <span class="option-number">Option #1</span>
      </div>
      <h2 class="option-name">Do Nothing</h2>
      <div class="option-body">
        <p class="list-heading">Advantages:</p>
        <ul class="points"><li>Stay married</li><li>No Life Changes</li></ul>
        <p class="list-heading">Disadvantages:</p>
        <ul class="points"><li>Remain unhappy, depressed, anxious</li><li>Money and assets may disappear</li><li>What is going to change?</li></ul>
      </div>
    </section>

    <section class="option even">
      <div class="option-tab">
        <svg width="183" height="35" aria-hidden="true"><polygon class="tab" points="0,0 120,0 130,17.5 120,35 0,35"/></svg>
        <span class="option-number">Option #2</span>
      </div>
      <h2 class="option-name">Go to Counseling</h2>
      <div class="option-body">
        <p class="list-heading">Advantages:</p>
        <ul class="points"><li>Reconcile Marriage</li><li>Help make a better life</li></ul>
        <p class="list-heading">Disadvantages:</p>
        <ul class="points"><li>Past issues are highlighted and may drudge up old wounds</li><li>It may just clarify the reasons you need to separate and/or divorce</li><li>Both parties mustbe invested and willing to participate</li></ul>
      </div>
    </section>

    <section class="option odd">
      <div class="option-tab">
        <svg width="183" height="35" aria-hidden="true"><polygon class="tab" points="0,0 120,0 130,17.5 120,35 0,35"/></svg>
        <span class="option-number">Option #3</span>
      </div>
      <h2 class="option-name">Do it Yourself</h2>
      <div class="option-body">
        <p class="list-heading">Advantages:</p>
        <ul class="points"><li>No attorney fees</li><li>You are your own attorney</li></ul>
        <p class="list-heading">Disadvantages:</p>
        <ul class="points"><li>People often find that what is “fair,” may in fact, not be truly fair</li><li>Often times, people do not know the risks</li><li>Complicated legal system</li><li>Unsure how to complete the necessary paperwork and meet the deadlines</li></ul>
      </div>
    </section>

    <section class="option even">
      <div class="option-tab">
        <svg width="183" height="35" aria-hidden="true"><polygon class="tab" points="0,0 120,0 130,17.5 120,35 0,35"/></svg>
        <span class="option-number">Option #4</span>
      </div>
      <h2 class="option-name">Limited Representation</h2>
      <div class="option-body">
        <p class="list-heading">Advantages:</p>
        <ul class="points"><li>Balance between going alone and our limited involvement in the case</li></ul>
        <p class="list-heading">Disadvantages:</p>
        <ul class="points"><li>Our terms may not benefit from our legal knowledge</li><li>The legal consequences of your legal documents will not be explained to you so that you can formulate a plan for handling the rest of your case</li><li>Your spouse or other parties may cause your legal fees to increase significantly without action on your part</li></ul>
      </div>
    </section>

    <section class="option odd">
      <div class="option-tab">
        <svg width="183" height="35" aria-hidden="true"><polygon class="tab" points="0,0 120,0 130,17.5 120,35 0,35"/></svg>
        <span class="option-number">Option #5</span>
      </div>
      <h2 class="option-name">Hire Us</h2>
      <div class="option-body">
        <p class="list-heading">Advantages:</p>
        <ul class="points"><li>Gain the full benefits of our experience</li><li>Have a team of Family Law focus attorneys</li><li>Often saves you or makes you money in the long run</li><li>Save you time, energy and stress</li></ul>
        <p class="list-heading">Disadvantages:</p>
        <ul class="points"><li>Initial cost</li></ul>
      </div>
    </section>
  </main>
</div>
</body>
</html>
```